Business Card & Logo Design

Originally the brief was for a card only - I now think it's probably better to include a logo design as well. PLease add $200 to the Budget of $210, Apologies for the inconvenience for thaos that have already submitted designs.

Lamp And Harbor Studios Pty Ltd is a video/dvd/ production company. Primarily corporate medium to high end. It's a one man operation that's been in business 20 years.

The name " Lamp and Harbor" is a primarily a reference to Lucien Marbeck film that's about film making. Shooting "Lamp and harbor" is also a technique employed by cinematographers to make scenes shot in daylight look like night.

See the design emphasising blue day/night tones but open to other ideas.

Main Text can either be Lamp and Harbor Studios or Lamp And Harbor.
Updates

Many thanks to all designers who submitted ideas for this brief.

Choosing between the designs was very difficult indeed.

I wish everyone the best and may the next job be yours!

Walter

Industry/Entity Type

Business

Requirements
Must have
• Text for card:
In Larger Print
Lamp And Harbor Studios or Lamp And Harbor
Walter Brenic
In Smaller Print
Lamp And Harbor Studios Pty Ltd.
17 Calder Lane
Kew Vale, VIC, 3152
P: 9734 2061
m: 0417 385 902
e: walterbrenic@examplemail.net

```html
<!DOCTYPE html>
<html lang="en">
<head>
<meta charset="utf-8">
<title>Lamp And Harbor Studios – Business Card</title>
<link rel="stylesheet" href="https://fonts.googleapis.com/css2?family=Nunito:wght@800;900&display=swap">
<style>
  :root {
    --page-bg: #ffffff;
    --sky-top: #c4e2f7;
    --sky-bottom: #6aaae0;
    --sea-top: #1f6fc2;
    --sea-bottom: #0b2e5e;
    --horizon-line: rgba(255, 255, 255, 0.75);
    --gold: #f7c815;
  }
  * { margin: 0; padding: 0; box-sizing: border-box; }
  html, body {
    width: 1200px;
    height: 900px;
    overflow: hidden;
    background: var(--page-bg);
  }
  .canvas {
    position: relative;
    width: 1200px;
    height: 900px;
  }
  .card {
    position: absolute;
    left: 128px;
    top: 188px;
    width: 944px;
    height: 524px;
    overflow: hidden;
    font-family: "Nunito", "Arial Rounded MT Bold", sans-serif;
  }
  .card-backdrop {
    position: absolute;
    inset: 0;
    width: 100%;
    height: 100%;
  }
  .brand {
    position: absolute;
    left: 32px;
    top: 120px;
    display: flex;
    align-items: center;
    gap: 12px;
  }
  .brand-dot {
    width: 28px;
    height: 28px;
    border-radius: 50%;
    background: var(--gold);
  }
  .brand-name {
    font-weight: 800;
    font-size: 31px;
    letter-spacing: 0.5px;
    color: var(--gold);
    text-transform: uppercase;
    line-height: 1;
  }
  .contact {
    position: absolute;
    left: 606px;
    top: 36px;
    list-style: none;
    font-weight: 800;
    font-size: 17px;
    line-height: 24.5px;
    color: var(--gold);
  }
  .holder {
    position: absolute;
    left: 0;
    right: 0;
    top: 310px;
    text-align: center;
    color: var(--gold);
  }
  .holder-name {
    font-weight: 900;
    font-size: 62px;
    line-height: 1;
    letter-spacing: 1px;
  }
  .holder-company {
    margin-top: 18px;
    font-weight: 800;
    font-size: 25px;
    line-height: 1;
  }
</style>
</head>
<body>
<div class="canvas">
  <section class="card">
    <svg class="card-backdrop" viewBox="0 0 944 524" preserveAspectRatio="none" aria-hidden="true">
      <defs>
        <linearGradient id="sea" x1="0" y1="0" x2="0" y2="1">
          <stop offset="0" stop-color="var(--sea-top)"/>
          <stop offset="1" stop-color="var(--sea-bottom)"/>
        </linearGradient>
        <linearGradient id="sky" x1="0" y1="0" x2="0" y2="1">
          <stop offset="0" stop-color="var(--sky-top)"/>
          <stop offset="1" stop-color="var(--sky-bottom)"/>
        </linearGradient>
      </defs>
      <rect width="944" height="524" fill="url(#sea)"/>
      <path d="M0 0 H944 V190 Q420 296 0 178 Z" fill="url(#sky)"/>
      <path d="M0 178 Q420 296 944 190" fill="none" stroke="var(--horizon-line)" stroke-width="2"/>
    </svg>

    <div class="brand">
      <span class="brand-dot"></span>
      <span class="brand-name">Lamp And Harbor</span>
    </div>

    <ul class="contact">
      <li>17 Calder Lane</li>
      <li>Kew Vale, VIC, 3152</li>
      <li>Phone: 9734 2061</li>
      <li>Mobile: 0417 385 902</li>
      <li>Email: walterbrenic@examplemail.net</li>
    </ul>

    <div class="holder">
      <h1 class="holder-name">Walter Brenic</h1>
      <p class="holder-company">Lamp And Harbor Studios Pty Ltd.</p>
    </div>
  </section>
</div>
</body>
</html>
```